依頼詳細
スタンダードメニューと特別ページメニューの作成。
スタンダードメニューはフランチャイズ店のようなイメージでお願いします。
参考サイト
https://www.mitsukeru-kensaku.example/search?q=%E5%B1%85%E9%85%92%E5%B1%8B%E3%83%A1%E3%83%8B%E3%83%A5%E3%83%BC&tbm=isch#imgrc=Qx7mTa2Lp9%3Bhttp%253A%252F%252Fimg.tarunikki.example%252Fphoto%252F5.jpg%3Bhttp%253A%252F%252Fkazuenikki.tarunikki.example%252F2011%252F10%252Fpost_17.html
この写真の上の部分の感じです。
料理写真と値段はエクセルで添付致します。
そのほかの写真はホームページから使用してください。
http://www.kurotori-shokudo.example/
料理の説明のあるものもありますので参考にして下さい。
エクセルシート1、2に分けて記載してあります。
よろしくお願い致します。

サイズ
A4
ページ数
6ページ
希望イメージ
シンプル 複雑
単色 カラフル
暗い 明るい
日常 高級
遊び心 厳粛
未来的 伝統的
女性的 男性的
希望する色
赤 黄 黒
納品ファイル
• イラストレーター形式 (.ai)
補足説明
かなり急いでいます。早ければ早いほど助かります。
写真を入れた簡単なイメージだけでも本日12時半頃までに頂けるとそのあとは2、3日の余裕はできます。
宜しくお願いします。

```html
<!DOCTYPE html>
<html lang="ja">
<head>
<meta charset="utf-8">
<title>黒鳥食堂 一品料理</title>
<link rel="stylesheet" href="https://fonts.googleapis.com/css2?family=Noto+Sans+JP:wght@500;700;900&family=Noto+Serif+JP:wght@900&display=swap">
<style>
  :root {
    --red: #d4141b;
    --deep-red: #9e0c10;
    --ink: #111;
    --panel: rgba(20, 18, 18, 0.86);
    --panel-line: #e9e3dc;
    --text: #fff;
    --cream: #f4efe6;
  }
  * { box-sizing: border-box; margin: 0; padding: 0; }
  html, body { width: 845px; height: 1200px; overflow: hidden; background: #2a1a12; }
  body { font-family: "Noto Sans JP", sans-serif; color: var(--text); }

  .menu-page { position: relative; width: 845px; height: 1200px; overflow: hidden; }

  .backdrop {
    position: absolute; inset: 0;
    background:
      radial-gradient(ellipse at 20% 30%, #b7743f 0%, transparent 45%),
      radial-gradient(ellipse at 80% 55%, #8d4a25 0%, transparent 50%),
      radial-gradient(ellipse at 30% 85%, #c08a52 0%, transparent 45%),
      linear-gradient(180deg, #6a3a1e 0%, #4a2714 60%, #6e3f22 100%);
  }

  .masthead {
    position: absolute; left: 0; top: 0; width: 845px; height: 178px;
    background: linear-gradient(180deg, rgba(250,247,240,0.97) 0%, rgba(240,232,220,0.92) 100%);
  }
  .tagline {
    position: absolute; left: 44px; top: 34px;
    font-family: "Noto Serif JP", serif; font-weight: 900;
    color: var(--red); font-size: 36px; line-height: 50px; text-align: right;
  }
  .shop-name-reading {
    position: absolute; left: 420px; top: 8px; width: 390px; text-align: center;
    color: var(--red); font-weight: 700; font-size: 20px; letter-spacing: 0.3em;
  }
  .shop-name {
    position: absolute; left: 380px; top: 36px;
    display: flex; align-items: center; gap: 18px;
  }
  .shop-name .mark { width: 26px; height: 26px; border-radius: 50%; background: var(--ink); }
  .shop-name span {
    font-weight: 900; font-size: 98px; line-height: 110px; color: var(--ink); letter-spacing: 0.02em;
  }

  .section-title {
    position: absolute; left: 212px; top: 178px; width: 420px; height: 76px;
    background: var(--red); padding: 7px;
  }
  .section-title h1 {
    height: 100%; background: var(--cream);
    color: var(--red); font-family: "Noto Serif JP", serif; font-weight: 900;
    font-size: 46px; letter-spacing: 0.25em; text-align: center; line-height: 62px;
    padding-left: 0.25em;
  }

  .price-panel {
    position: absolute; background: var(--panel);
    border: 2px solid var(--panel-line); border-radius: 14px;
    padding: 62px 22px 0 28px;
  }
  .price-band {
    position: absolute; left: 12px; top: 4px;
    font-weight: 900; font-size: 40px; color: var(--red); letter-spacing: 0.02em;
    text-shadow: -2px -2px 0 #fff, 2px -2px 0 #fff, -2px 2px 0 #fff, 2px 2px 0 #fff, 0 2px 0 #fff, 0 -2px 0 #fff;
  }
  .price-band::after {
    content: ""; position: absolute; left: -6px; right: -40px; bottom: 6px; height: 14px;
    background: linear-gradient(90deg, var(--deep-red), rgba(158,12,16,0)); z-index: -1;
  }

  .dish-list { list-style: none; }
  .dish {
    display: flex; align-items: baseline; font-weight: 700; font-size: 19px;
    height: 42px; line-height: 42px; white-space: nowrap;
  }
  .dish::before { content: "・"; }
  .dish .leader {
    flex: 1; margin: 0 6px; border-bottom: 3px dotted rgba(255,255,255,0.85);
    transform: translateY(-8px); min-width: 20px;
  }
  .dish-list.short .dish { flex: none; }

  .photo {
    position: absolute; border-radius: 3px;
  }
  .photo-caption {
    position: absolute; font-size: 13px; font-weight: 700; color: var(--text); text-align: center;
  }

  .panel-190 { left: 23px; top: 268px; width: 378px; height: 296px; }
  .panel-190 .dish-list { width: 300px; }
  .panel-190 .dish { height: 58px; line-height: 58px; }

  .panel-320 { left: 423px; top: 268px; width: 400px; height: 296px; }
  .panel-320 .dish { height: 62px; line-height: 62px; }
  .panel-320 .dish.fixed { width: 190px; }
  .panel-320 .photo { left: 228px; top: 62px; width: 160px; height: 64px;
    background: radial-gradient(ellipse at 50% 50%, #7d9a3a 0%, #4f6b1f 60%, #2a3a12 100%); }
  .panel-320 .photo-caption { left: 228px; top: 128px; width: 160px; }

  .panel-390 { left: 23px; top: 578px; width: 406px; height: 604px; }
  .panel-390 .dish { height: 52px; line-height: 52px; }
  .panel-390 .dish.narrow { width: 238px; }
  .panel-390 .photo { left: 262px; top: 134px; width: 130px; height: 92px;
    background: radial-gradient(ellipse at 50% 55%, #c98b3d 0%, #8c5520 55%, #3d2410 100%); }
  .panel-390 .photo-caption { left: 262px; top: 228px; width: 130px; }

  .panel-450 { left: 445px; top: 578px; width: 378px; height: 604px; }
  .panel-450 .dish { height: 52px; line-height: 52px; }
  .panel-450 .photo { left: 88px; top: 388px; width: 200px; height: 150px;
    background: radial-gradient(ellipse at 50% 55%, #f3d46a 0%, #e0b23a 55%, #6f6a52 100%); }
  .panel-450 .photo-caption { left: 88px; top: 546px; width: 200px; font-size: 15px; }
</style>
</head>
<body>
<main class="menu-page">
  <div class="backdrop" role="img" aria-label="炭火焼きの鶏料理の写真"></div>

  <header class="masthead">
    <p class="tagline">宮崎地鶏専門店<br>本格炭火焼き</p>
    <p class="shop-name-reading">くろとりしょくどう</p>
    <div class="shop-name"><i class="mark"></i><span>黒鳥食堂</span></div>
  </header>

  <div class="section-title"><h1>一品料理</h1></div>

  <section class="price-panel panel-190">
    <h2 class="price-band">ALL 190円</h2>
    <ul class="dish-list">
      <li class="dish">まるきゅう<i class="leader"></i>190円</li>
      <li class="dish">えだまめ<i class="leader"></i>190円</li>
      <li class="dish">ざる豆腐<i class="leader"></i>190円</li>
    </ul>
  </section>

  <section class="price-panel panel-320">
    <h2 class="price-band">ALL 320円</h2>
    <ul class="dish-list">
      <li class="dish fixed">梅くらげ<i class="leader"></i>320円</li>
      <li class="dish fixed">ジャコおろし 320円</li>
      <li class="dish">焼き茶豆（店長一押し）<i class="leader"></i>320円</li>
    </ul>
    <div class="photo" role="img" aria-label="焼き茶豆の写真"></div>
    <p class="photo-caption">店長一押しの焼き茶豆</p>
  </section>

  <section class="price-panel panel-390">
    <h2 class="price-band">ALL 390円</h2>
    <ul class="dish-list">
      <li class="dish">特製だし巻き玉子<i class="leader"></i>390円</li>
      <li class="dish narrow">ホッキ貝サラダ 390円</li>
      <li class="dish narrow">豊浜産もずく 390円</li>
      <li class="dish narrow">たっぷりキャベツ 390円</li>
      <li class="dish">プチトマトの串焼き<i class="leader"></i>390円</li>
      <li class="dish">特製鶏そぼ<i class="leader"></i>390円</li>
      <li class="dish">にんにくのオイル焼き<i class="leader"></i>390円</li>
      <li class="dish">特製チャンジャ<i class="leader"></i>390円</li>
      <li class="dish">鶏なんこつから揚げ<i class="leader"></i>390円</li>
      <li class="dish">ポテトフライ<i class="leader"></i>390円</li>
    </ul>
    <div class="photo" role="img" aria-label="鶏なんこつから揚げの写真"></div>
    <p class="photo-caption">鶏なんこつから揚げ</p>
  </section>

  <section class="price-panel panel-450">
    <h2 class="price-band">ALL 450円</h2>
    <ul class="dish-list">
      <li class="dish">特製だし巻き玉子<i class="leader"></i>450円</li>
      <li class="dish">特製鶏たで<i class="leader"></i>450円</li>
      <li class="dish">長芋のガーリックバター<i class="leader"></i>450円</li>
      <li class="dish">牛すじの煮込み<i class="leader"></i>450円</li>
      <li class="dish">砂肝ポン酢<i class="leader"></i>450円</li>
      <li class="dish">イカゲソの唐揚げ<i class="leader"></i>450円</li>
    </ul>
    <div class="photo" role="img" aria-label="特製だし巻き玉子の写真"></div>
    <p class="photo-caption">特製だし巻き玉子</p>
  </section>
</main>
</body>
</html>
```